"The Velvet Ledge" nails, eyelash extensions and hair extensions. Need an eye catching design for bu

Need an eye catching design focusing on eyelash extensions, nail extensions and hair extensions. I like the colour green, black, glitter, pink?! need the design to be innovative and 'POP'. I'd like more emphasis on lashes and nails.
I'd like the business name and my phone number on the front of card.
Would really like something different and unique.
"The Velvet Ledge"
Nails, Eyelash & Hair Extensions
Mira
0471526093

Target Market(s)

20-40

Industry/Entity Type

Beauty Salon

Contact Information for Business Card

Id like my business name, My name and phone number on the front of card
"The Velvet Ledge".
Mira.
0471526093.
Id like some catchy design involving long lashes with possibly glitter, long hair and nails. Id like the lashes to be the first thing you see at first glance. I'm open to your creative flair. Just need the business card design to 'POP'! I like the colours green, black, pink, silver or gold glitter. wether it's pop art, 3d drawn pictures, isolated pics of lash, nails or hair, card design could be in black and white with isolated colours added..i'm open to your creative flair. use a font which stands out and easy to read.
(The back of the card will be used for writing appointment times.)

Font styles to use
Serif

Colors
6b449b
e667a6
25b39d

Requirements
Must have
• Long lashes, hair, nails.
• one sided
Nice to have
• bright catchy colours, innovative, uniqueness

```html
<!DOCTYPE html>
<html lang="en">
<head>
<meta charset="utf-8">
<title>The Velvet Ledge – Business Card</title>
<link href="https://fonts.googleapis.com/css2?family=Didact+Gothic&family=Quicksand:wght@300;400&display=swap" rel="stylesheet">
<style>
  :root {
    --page-bg: #ececec;
    --card-pink: #eb1e79;
    --ink-dark: #1a1016;
    --ink-light: #ffffff;
    --art-silver: #d9d4d8;
    --art-pink: #f06aa6;
  }
  html, body {
    margin: 0;
    padding: 0;
    width: 1200px;
    height: 1021px;
    overflow: hidden;
    background: var(--page-bg);
  }
  .card {
    position: absolute;
    left: 100px;
    top: 187px;
    width: 1000px;
    height: 647px;
    background: var(--card-pink);
    box-shadow: 0 10px 30px rgba(0,0,0,0.18);
  }
  .card__art {
    position: absolute;
    left: 370px;
    top: 120px;
    width: 250px;
    height: 200px;
    border-radius: 10px;
    background: radial-gradient(ellipse at 50% 45%, var(--art-silver) 0%, var(--art-pink) 80%);
    opacity: 0.55;
  }
  .card__name {
    position: absolute;
    left: 0;
    right: 0;
    top: 360px;
    margin: 0;
    display: flex;
    justify-content: center;
    align-items: baseline;
    gap: 20px;
    font-family: "Didact Gothic", sans-serif;
    font-weight: 400;
    font-size: 62px;
    letter-spacing: 2px;
    line-height: 1.2;
    white-space: nowrap;
  }
  .card__name-lead { color: var(--ink-light); }
  .card__name-word { color: var(--ink-dark); }
  .card__contact {
    position: absolute;
    left: 0;
    right: 0;
    top: 468px;
    margin: 0;
    text-align: center;
    font-family: "Quicksand", sans-serif;
    font-weight: 300;
    font-size: 42px;
    letter-spacing: 1px;
    line-height: 1.2;
    white-space: nowrap;
  }
  .card__person { color: var(--ink-light); }
  .card__phone { color: var(--ink-dark); }
</style>
</head>
<body>
  <div class="card">
    <div class="card__art" role="img" aria-label="Silver line illustration of a woman in profile with long flowing hair, touching her chin with long manicured nails"></div>
    <h1 class="card__name"><span class="card__name-lead">The</span> <span class="card__name-word">Velvet</span> <span class="card__name-word">Ledge</span></h1>
    <p class="card__contact"><span class="card__person">Mira.</span> <span class="card__phone">0471526093</span></p>
  </div>
</body>
</html>
```